Updating our Raw Materials Brochure

Please update and modify (to add more space for the additional text) the brochure designed for us in January (see attached file) so we can circulate a May 2021 version. Thanks and hope your family is OK despite the terrible tragedy going on with Covid-19 in India. Best wishes!

```html
<!DOCTYPE html>
<html lang="en">
<head>
<meta charset="utf-8">
<title>Raw Materials May 2021 Market Update</title>
<link href="https://fonts.googleapis.com/css2?family=Montserrat:wght@500;700;800&family=Open+Sans:wght@400;600;700&display=swap" rel="stylesheet">
<style>
  :root {
    --red: #e0202b;
    --red-dark: #b5141d;
    --ink: #1d1d1f;
    --charcoal: #232326;
    --text: #3a3a3c;
    --rule: #c9c9cc;
    --paper: #ffffff;
    --backdrop: #e6e6e8;
    --blue: #2f6fb8;
    --orange: #e8812a;
    --pink: #c0306a;
  }
  * { box-sizing: border-box; margin: 0; padding: 0; }
  html, body { width: 900px; height: 1200px; overflow: hidden; }
  body {
    background: var(--backdrop);
    font-family: "Open Sans", Arial, sans-serif;
    color: var(--text);
    position: relative;
  }
  .page {
    position: absolute;
    top: 300px;
    width: 430px;
    height: 590px;
    background: var(--paper);
    box-shadow: 0 4px 14px rgba(0,0,0,.18);
    overflow: hidden;
  }
  .page--front { left: 14px; }
  .page--back { left: 456px; }

  .brand {
    position: absolute;
    display: flex; align-items: center; gap: 5px;
    font-family: "Montserrat", sans-serif;
    font-weight: 800; font-size: 11px; color: var(--ink);
    letter-spacing: .3px;
  }
  .brand__mark { width: 12px; height: 12px; border-radius: 50%; background: var(--ink); }

  .hero {
    position: absolute; left: 0; top: 46px; width: 430px; height: 118px;
  }
  .hero__title {
    position: absolute; left: 150px; top: 68px; text-align: center;
    font-family: "Montserrat", sans-serif; font-weight: 800;
    color: #fff; font-size: 17px; line-height: 1.05;
  }
  .hero__title .accent { color: var(--red); font-size: 15px; display: block; }

  .call-box {
    position: absolute; right: 0; top: 14px; width: 190px; height: 34px;
    background: var(--red);
    clip-path: polygon(10% 0, 100% 0, 100% 100%, 0 100%);
    color: #fff; font-family: "Montserrat", sans-serif; font-weight: 700;
    font-size: 9px; line-height: 1.15;
    display: flex; align-items: center; gap: 6px; padding-left: 30px;
  }
  .call-box svg { width: 16px; height: 16px; }

  .column { position: absolute; }
  .section-head {
    background: var(--red); color: #fff;
    font-family: "Montserrat", sans-serif; font-weight: 800;
    font-size: 10px; padding: 5px 8px; margin-bottom: 6px;
    clip-path: polygon(0 0, 100% 0, 94% 100%, 0 100%);
    line-height: 1.15;
  }
  .sub-head {
    font-family: "Montserrat", sans-serif; font-weight: 700;
    color: var(--ink); font-size: 8px; line-height: 1.2; margin: 4px 0 3px;
  }
  .body-text {
    font-size: 5.6px; line-height: 1.45; text-align: justify; margin-bottom: 5px;
  }
  .chart {
    border: 1px solid var(--rule); background: #fff; margin: 4px 0 6px;
  }
  .chart svg { display: block; width: 100%; }

  .footer {
    position: absolute; left: 0; bottom: 0; width: 430px; height: 30px;
    background: var(--charcoal);
  }
  .footer__web {
    position: absolute; right: 0; top: 0; height: 30px; width: 200px;
    background: var(--red);
    clip-path: polygon(8% 0, 100% 0, 100% 100%, 0 100%);
    color: #fff; font-family: "Montserrat", sans-serif; font-weight: 700;
    font-size: 9px; display: flex; align-items: center; justify-content: center;
  }
  .footer__call {
    position: absolute; left: 16px; top: 0; height: 30px;
    color: #fff; font-family: "Montserrat", sans-serif; font-weight: 800;
    font-size: 10px; display: flex; align-items: center; gap: 6px;
  }
  .footer__call svg { width: 14px; height: 14px; }

  .title-band {
    position: absolute; right: 0; top: 20px; width: 250px; height: 44px;
    background: var(--red);
    clip-path: polygon(9% 0, 100% 0, 100% 100%, 0 100%);
    color: #fff; text-align: center;
    font-family: "Montserrat", sans-serif; font-weight: 800;
    font-size: 11px; line-height: 1.2; padding: 9px 0 0 24px;
  }
  .page--back .footer__web { width: 170px; }
</style>
</head>
<body>

<section class="page page--front">
  <div class="brand" style="left:18px; top:16px;"><span class="brand__mark"></span>KESTREL POLYMERS</div>

  <div class="call-box">
    <svg viewBox="0 0 24 24" aria-hidden="true"><circle cx="12" cy="12" r="11" fill="none" stroke="#fff" stroke-width="1.6"/><path d="M8 7c1 0 1.5 2 1.5 2.6 0 .6-.9 1-.7 1.6.5 1.4 1.7 2.6 3 3 .6.2 1-.7 1.6-.7.6 0 2.6.5 2.6 1.5 0 1-1.3 2-2.3 2C10 17 7 14 7 9.3 7 8.3 7.5 7 8 7z" fill="#fff"/></svg>
    <span>CALL US AT<br>800-555-0142</span>
  </div>

  <div class="hero">
    <svg width="430" height="118" role="img" aria-label="Photograph of Earth from space at sunrise, dark blue with a glowing horizon">
      <defs>
        <radialGradient id="glow" cx="30%" cy="100%" r="70%">
          <stop offset="0" stop-color="#f4c77a"/>
          <stop offset=".15" stop-color="#3c6aa0"/>
          <stop offset=".6" stop-color="#0f1b2c"/>
          <stop offset="1" stop-color="#07090f"/>
        </radialGradient>
      </defs>
      <polygon points="0,18 430,0 430,92 0,118" fill="url(#glow)"/>
    </svg>
    <div class="hero__title">RAW MATERIALS<br>MAY 2021<span class="accent">MARKET UPDATE</span></div>
  </div>

  <div class="column" style="left:16px; top:172px; width:194px;">
    <div class="section-head">GLOBAL SHORTAGES</div>
    <p class="body-text">As the recovery builds momentum more manufacturers are trying to buy extra materials to prevent running out. Nearly all inputs are affected and there seems to be no end in sight as supply is unable to keep up with demand.</p>
    <p class="body-text">The situation has been complicated by a growing list of disasters. Starting with the deep freeze and blackouts wiping out energy and petrochemicals operations in February, the Suez canal back up in March then hackers bringing down the largest US pipeline this month.</p>
    <p class="body-text">US GDP increased at a 10.7% annual rate or $554.2 billion in current dollars (adjusted to 6.4% for inflation) in the first quarter. Demand seems to be driven by personal income growing $2.4 trillion (up 59%) from increased government social benefits and pandemic relief programs. Expectations are it will continue as personal savings were $4.12 trillion (up 83% the fourth quarter) driving personal savings to 21%.</p>
    <p class="body-text">The trailing 12-month Producer Price Index and Consumer Price Index were up 6.2% and 4.2% respectively. These should go higher as the trailing 4-months averages are 10.2% and 6.3% respectively. Our procurement team is focused on leveraging our global supply position and growing demand so we will continue to deliver you the most competitive costs available despite these conditions.</p>
    <div class="chart">
      <svg viewBox="0 0 194 100">
        <text x="6" y="9" font-size="4.5" font-weight="700" fill="#333">Chart 1: 12-month percent change in CPI, Apr 2020 - Apr 2021</text>
        <g stroke="#e3e3e3" stroke-width=".5">
          <line x1="16" y1="20" x2="188" y2="20"/><line x1="16" y1="40" x2="188" y2="40"/><line x1="16" y1="60" x2="188" y2="60"/><line x1="16" y1="80" x2="188" y2="80"/>
        </g>
        <polyline fill="none" stroke="#9a2a4a" stroke-width=".8" points="20,70 33,72 46,66 59,62 72,58 85,56 98,57 111,55 124,52 137,50 150,46 163,38 176,22"/>
        <polyline fill="none" stroke="#3a5fb0" stroke-width=".8" points="20,78 33,84 46,74 59,66 72,62 85,61 98,63 111,62 124,60 137,58 150,52 163,44 176,14"/>
        <g font-size="4" fill="#666">
          <text x="16" y="90">Apr20</text><text x="60" y="90">Aug</text><text x="104" y="90">Dec</text><text x="168" y="90">Apr21</text>
        </g>
        <text x="70" y="97" font-size="4" fill="#555">All items — All items less food and energy</text>
      </svg>
    </div>
  </div>

  <div class="column" style="left:222px; top:172px; width:194px;">
    <div class="section-head">KEY CONSTRAINTS</div>
    <h3 class="sub-head">Ethylene Shortage Drives Prices Higher</h3>
    <p class="body-text">Contractual prices for Ethylene (key feedstock for water based and hot melt adhesives) increased 56% from 2020 to a 7-year high of $0.47/lb in March as multiple severe weather cracker outages driven by the deep freeze in February forced 70% capacity offline. Restarting production has been difficult as so many sites were damaged simultaneously.</p>
    <div class="chart">
      <svg viewBox="0 0 194 100">
        <text x="6" y="9" font-size="4.5" font-weight="700" fill="#333">Chart 2: 12-month percent change in PPI, Apr 2020 - Apr 2021</text>
        <g stroke="#e3e3e3" stroke-width=".5">
          <line x1="16" y1="20" x2="188" y2="20"/><line x1="16" y1="40" x2="188" y2="40"/><line x1="16" y1="60" x2="188" y2="60"/><line x1="16" y1="80" x2="188" y2="80"/>
        </g>
        <polyline fill="none" stroke="#9a2a4a" stroke-width=".8" points="20,74 33,70 46,64 59,58 72,54 85,50 98,48 111,46 124,44 137,40 150,36 163,30 176,18"/>
        <polyline fill="none" stroke="#3a5fb0" stroke-width=".8" points="20,80 33,82 46,72 59,64 72,60 85,56 98,54 111,52 124,50 137,48 150,44 163,36 176,12"/>
        <g font-size="4" fill="#666">
          <text x="16" y="90">Apr20</text><text x="60" y="90">Aug</text><text x="104" y="90">Dec</text><text x="168" y="90">Apr21</text>
        </g>
        <text x="70" y="97" font-size="4" fill="#555">All items — All items less food and energy</text>
      </svg>
    </div>
    <h3 class="sub-head">Vinyl Acetate Monomer (VAM) – Key Ingredient for Water Based Adhesives</h3>
    <p class="body-text">VAM shortages became severe following the February winter storm driving prices up 128% since Jan-2021. All three US suppliers (Northfield Chemical, Arcadia and Brightwater) declared force majeure and all four production sites were shut down. They were stuck in varying stages of restarting and ramping up to full rates for nearly 3 months so supplies remain limited and that is expected to continue through Q2 with demand currently outstripping supply.</p>
  </div>

  <div class="footer">
    <div class="footer__web">www.kestrelpolymers.com</div>
  </div>
</section>

<section class="page page--back">
  <div class="brand" style="left:18px; top:30px;"><span class="brand__mark"></span>KESTREL POLYMERS</div>
  <div class="title-band">RAW MATERIALS MAY 2021<br>MARKET UPDATE</div>

  <div class="column" style="left:16px; top:74px; width:194px;">
    <div class="section-head">LOGISTICS LIMITATIONS<br>VS. DEMAND GROWTH</div>
    <p class="body-text">The ramp up in production of consumer and industrial goods while consumers still rely more on at home delivery or pick up from stores (which require more trucks and warehousing) has driven unprecedented logistics tightness.</p>
    <div class="chart">
      <svg viewBox="0 0 194 96">
        <text x="6" y="9" font-size="5" font-weight="700" fill="#222">A Logistical Nightmare</text>
        <text x="6" y="15" font-size="3.8" fill="#555">Transport, storage and inventory costs are near record highs</text>
        <g font-size="3.6" fill="#555">
          <line x1="6" y1="20" x2="12" y2="20" stroke="#111"/><text x="14" y="21">Transportation</text>
          <line x1="44" y1="20" x2="50" y2="20" stroke="var(--pink)"/><text x="52" y="21">Warehousing</text>
          <line x1="82" y1="20" x2="88" y2="20" stroke="var(--blue)"/><text x="90" y="21">Inventories</text>
        </g>
        <line x1="8" y1="62" x2="170" y2="62" stroke="#d9b338" stroke-dasharray="2 1.5" stroke-width=".6"/>
        <polyline fill="none" stroke="var(--pink)" stroke-width=".8" points="8,50 20,46 32,52 44,48 56,44 68,50 80,54 92,48 104,50 116,46 128,40 140,38 152,30 164,26"/>
        <polyline fill="none" stroke="var(--blue)" stroke-width=".8" points="8,58 20,60 32,56 44,62 56,58 68,64 80,66 92,58 104,54 116,48 128,44 140,40 152,34 164,28"/>
        <polyline fill="none" stroke="#111" stroke-width=".9" points="8,60 20,64 32,62 44,68 56,66 68,70 80,72 92,50 104,66 116,40 128,36 140,34 152,28 164,22"/>
        <g font-size="3.6" fill="#555">
          <text x="174" y="28">75</text><text x="174" y="63">50</text><text x="174" y="82">25</text>
          <text x="30" y="86">2019</text><text x="92" y="86">2020</text><text x="150" y="86">2021</text>
        </g>
        <text x="6" y="93" font-size="3.4" fill="#777">Source: Freight Activity Gauge, 50 marks expansion vs. contraction</text>
      </svg>
    </div>
    <p class="body-text">Capacity is constrained by slowed construction in vehicles (chips and other materials shortages) as traditional channels are idled (shopping malls, etc.). Spot Van rates were up 58.1% versus April 2020 as outages cause chain reactions. Currently there is a traffic jam of 771 barges accumulated on the lower Mississippi due to a fractured bridge, so expectations are this will continue until year end.</p>
    <div class="chart">
      <svg viewBox="0 0 194 118">
        <text x="70" y="10" font-size="5" font-weight="700" fill="#222">Transportation Prices</text>
        <g fill="var(--blue)">
          <rect x="10" y="88" width="5" height="16"/><rect x="17" y="90" width="5" height="14"/><rect x="24" y="89" width="5" height="15"/><rect x="31" y="87" width="5" height="17"/>
          <rect x="38" y="86" width="5" height="18"/><rect x="45" y="88" width="5" height="16"/><rect x="52" y="85" width="5" height="19"/><rect x="59" y="84" width="5" height="20"/>
          <rect x="66" y="80" width="5" height="24"/><rect x="73" y="76" width="5" height="28"/><rect x="80" y="70" width="5" height="34"/><rect x="87" y="72" width="5" height="32"/>
          <rect x="94" y="66" width="5" height="38"/><rect x="101" y="58" width="5" height="46"/><rect x="108" y="50" width="5" height="54"/><rect x="115" y="44" width="5" height="60"/>
          <rect x="122" y="40" width="5" height="64"/><rect x="129" y="36" width="5" height="68"/><rect x="136" y="32" width="5" height="72"/><rect x="143" y="28" width="5" height="76"/>
          <rect x="150" y="24" width="5" height="80"/><rect x="157" y="22" width="5" height="82"/><rect x="164" y="20" width="5" height="84"/><rect x="171" y="18" width="5" height="86"/>
        </g>
        <path d="M12,86 C40,88 60,86 80,74 S110,40 130,34 S165,20 176,18" fill="none" stroke="var(--red)" stroke-width="1"/>
        <line x1="8" y1="104" x2="182" y2="104" stroke="#999" stroke-width=".5"/>
        <g font-size="3.4" fill="#666">
          <text x="8" y="112">Apr-19</text><text x="60" y="112">Dec-19</text><text x="112" y="112">Aug-20</text><text x="162" y="112">Apr-21</text>
        </g>
      </svg>
    </div>
  </div>

  <div class="column" style="left:222px; top:74px; width:194px;">
    <div class="chart">
      <svg viewBox="0 0 194 128">
        <text x="80" y="12" font-size="6" fill="#555">VAM Index</text>
        <g stroke="#e6e6e6" stroke-width=".5">
          <line x1="30" y1="22" x2="188" y2="22"/><line x1="30" y1="38" x2="188" y2="38"/><line x1="30" y1="54" x2="188" y2="54"/><line x1="30" y1="70" x2="188" y2="70"/><line x1="30" y1="86" x2="188" y2="86"/><line x1="30" y1="102" x2="188" y2="102"/>
        </g>
        <g font-size="4" fill="#666" text-anchor="end">
          <text x="27" y="24">$2,300</text><text x="27" y="40">$1,900</text><text x="27" y="56">$1,500</text><text x="27" y="72">$1,100</text><text x="27" y="88">$900</text><text x="27" y="104">$500</text>
        </g>
        <polyline fill="none" stroke="var(--orange)" stroke-width="1.1" points="40,96 60,92 80,88 100,86 120,82 140,76 155,60 170,22"/>
        <g font-size="4" fill="#666">
          <text x="36" y="112">Oct-20</text><text x="70" y="112">Dec-20</text><text x="104" y="112">Feb-21</text><text x="150" y="112">Apr-21</text>
        </g>
        <text x="70" y="122" font-size="4" fill="#555">Index VAM FOB Spot Low ($/mt)</text>
      </svg>
    </div>
    <h3 class="sub-head">Polyethylene and Polyurethane Prices near record highs</h3>
    <p class="body-text">About 42% of US oil refining capacity went offline in February (~5.5m barrels/day) but it has recovered to over 98% by last week. The shortages this created downstream continue to create spot outages of critical inputs resulting in reduced operating rates at our suppliers.</p>
    <p class="body-text">For example, Polyethylene polymers (critical in hot melt adhesives) increased 39% this year plus Benzene increased 10% in April and Polyether Polyols (key feedstock for polyurethanes) are on 75% sales allocation because of limited domestic materials and difficulty bringing in imports from marine transport shortages. As a result, the price index for rubbers and plastics is up 9% since January and is still rising.</p>
    <div class="chart" style="background:#eef2f8;">
      <svg viewBox="0 0 194 96">
        <text x="6" y="9" font-size="4.5" font-weight="700" fill="#2f4f7f">Price Index: Rubber and Plastic Products</text>
        <rect x="150" y="14" width="36" height="66" fill="#f0ecd8"/>
        <g stroke="#d6dce6" stroke-width=".5">
          <line x1="14" y1="24" x2="186" y2="24"/><line x1="14" y1="44" x2="186" y2="44"/><line x1="14" y1="64" x2="186" y2="64"/>
        </g>
        <polyline fill="none" stroke="var(--blue)" stroke-width=".9" points="14,74 30,70 46,66 62,58 78,54 94,50 110,46 126,44 140,42 150,40 160,34 170,26 180,16"/>
        <rect x="14" y="82" width="172" height="5" fill="#c9d4e6"/>
        <g font-size="3.6" fill="#666"><text x="14" y="94">2010</text><text x="90" y="94">2015</text><text x="166" y="94">2021</text></g>
      </svg>
    </div>
  </div>

  <div class="footer">
    <div class="footer__call">
      <span>CALL US AT</span>
      <svg viewBox="0 0 24 24" aria-hidden="true"><circle cx="12" cy="12" r="11" fill="var(--red)"/><path d="M8 7c1 0 1.5 2 1.5 2.6 0 .6-.9 1-.7 1.6.5 1.4 1.7 2.6 3 3 .6.2 1-.7 1.6-.7.6 0 2.6.5 2.6 1.5 0 1-1.3 2-2.3 2C10 17 7 14 7 9.3 7 8.3 7.5 7 8 7z" fill="#fff"/></svg>
      <span>800-555-0142</span>
    </div>
    <div class="footer__web">www.kestrelpolymers.com</div>
  </div>
</section>

</body>
</html>
```